#VESSA

#Vessa is the business name. I need a marketing brochure to show potential clients. The concept is providing the restaurant trade and function centres with volume wine in large wine casks and then on-sell by the glass or in varying carafe sizes. The advantages will be outlined in the file provided I want to introduce the concept and demonstrate the advantages visusally

Industry/Entity Type

Restaurant

```html
<!DOCTYPE html>
<html lang="en">
<head>
<meta charset="utf-8">
<title>Vessa — Wine for the Restaurant Trade</title>
<link rel="stylesheet" href="https://fonts.googleapis.com/css2?family=Didact+Gothic&display=swap">
<style>
  :root {
    --silk-deep: #4a0a0c;
    --silk-red: #8e1a17;
    --silk-salmon: #c98977;
    --silk-grey: #8c7a78;
    --band-black: #000000;
    --bottle-dark: #140709;
    --text-white: #ffffff;
    --text-wine: #7a1212;
  }
  html, body {
    margin: 0;
    padding: 0;
    overflow: hidden;
    background: #ffffff;
  }
  .brochure {
    position: relative;
    width: 1200px;
    height: 847px;
    overflow: hidden;
    font-family: "Didact Gothic", "Century Gothic", sans-serif;
    color: var(--text-white);
  }
  .silk-backdrop {
    position: absolute;
    inset: 0;
    background:
      radial-gradient(ellipse 420px 520px at 140px 330px, var(--silk-red) 0%, rgba(142,26,23,0) 70%),
      radial-gradient(ellipse 520px 300px at 820px 560px, var(--silk-grey) 0%, rgba(140,122,120,0) 75%),
      linear-gradient(100deg, var(--silk-deep) 0%, var(--silk-red) 22%, #a6443a 38%, var(--silk-salmon) 55%, #b98a7f 80%, var(--silk-salmon) 100%);
  }
  .title-band {
    position: absolute;
    left: 474px;
    top: 0;
    width: 726px;
    height: 238px;
    background: var(--band-black);
  }
  .brand-name {
    position: absolute;
    left: 520px;
    top: 22px;
    margin: 0;
    font-family: "Didact Gothic", "Century Gothic", sans-serif;
    font-weight: 400;
    font-size: 170px;
    line-height: 1;
    color: var(--text-white);
  }
  .bottle {
    position: absolute;
    left: 150px;
    top: 10px;
    width: 190px;
    height: 920px;
    background: var(--bottle-dark);
    border-radius: 60px 60px 6px 6px;
    transform: rotate(22deg);
    transform-origin: 50% 50%;
  }
  .tagline {
    position: absolute;
    left: 486px;
    top: 302px;
    margin: 0;
    width: 710px;
    font-size: 31px;
    line-height: 38px;
    color: var(--text-wine);
  }
  .advantages {
    position: absolute;
    left: 486px;
    top: 418px;
    width: 710px;
  }
  .advantages-intro {
    margin: 0 0 2px;
    font-size: 21px;
    line-height: 32px;
  }
  .advantages-list {
    list-style: none;
    margin: 0;
    padding: 0 0 0 72px;
    font-size: 22.5px;
  }
  .advantages-list li {
    line-height: 31.6px;
    padding-left: 20px;
    text-indent: -20px;
  }
  .advantages-list li::before {
    content: "»";
    display: inline-block;
    width: 20px;
    text-indent: 0;
  }
  .product-notes {
    position: absolute;
    left: 360px;
    top: 745px;
    margin: 0;
    font-size: 19.5px;
    line-height: 26px;
    white-space: nowrap;
  }
</style>
</head>
<body>
  <main class="brochure">
    <div class="silk-backdrop" role="img" aria-label="Draped silk fabric in deep red fading to soft salmon"></div>
    <div class="title-band"></div>
    <h1 class="brand-name">Vessa</h1>
    <div class="bottle" role="img" aria-label="Bottle of red wine with blank label"></div>

    <p class="tagline">Providing the restaurant trade with a more effective,<br>economical and sustainable alternative to wine retail.</p>

    <section class="advantages">
      <p class="advantages-intro">The advantages of using #VESSA concept:</p>
      <ul class="advantages-list">
        <li>The cask wine uses less storage space</li>
        <li>Eco friendly, no glass.</li>
        <li>Larger quantity better margins</li>
        <li>Longer shelf life</li>
        <li>No wastage</li>
        <li>More Hygienic</li>
        <li>Wine sourced from reputable growers in well-known regions<br>of New Zealand, Barossa Valley and Tasmania.</li>
      </ul>
    </section>

    <p class="product-notes">
      Cask sizes will start from 10ltrs and up to 22ltrs<br>
      Aesthetic Urns or Wine barrels to hide cask that will come in either 15ltr, 25ltr and will fit all cask sizes.<br>
      Carafe glassware available too: in 250ml, 500ml and 1000ml sizes.
    </p>
  </main>
</body>
</html>
```